Briefpapier, Visitenkarten, Bindemappe, Brieumschläge....
Zielgruppe
Steuerberatung vorwiegen für Unternehmer
Aufgabenstellung
Ein Logo ist bereits vorhanden (siehe Analgen) kann aber gerne auch bei einer guten Idee modernisiert werden. Ganz ein neues Logo möchte ich meinen Kunden jedoch ersparen, da ich es erst von zwei Jahren gewechselt habe. Grundfarbe grün wie Pantone 2293 C.
Als Anhaltspunkt was derzeit bei im Einsatz ist, habe ich die entsprechenden Dateien hochgeladen.

```html
<!DOCTYPE html>
<html lang="de">
<head>
<meta charset="utf-8">
<title>Briefpapier – Henrik Aldor</title>
<link href="https://fonts.googleapis.com/css2?family=PT+Sans:wght@400;700&display=swap" rel="stylesheet">
<style>
  :root {
    --page: #ffffff;
    --backdrop: #ffffff;
    --ink: #1a1a1a;
    --brand-grey: #56605f;
    --pattern-tone: #e4e4e4;
    --pattern-edge: #d6d6d6;
    --brand-green: #9bd11f;
    --brand-green-light: #c9ec6a;
  }
  * { margin: 0; padding: 0; box-sizing: border-box; }
  html, body {
    width: 856px; height: 1200px; overflow: hidden;
    background: var(--backdrop);
    font-family: "PT Sans", Arial, sans-serif;
    color: var(--ink);
  }
  .letterhead {
    position: absolute; left: 11px; top: 11px;
    width: 834px; height: 1179px;
    background: var(--page);
    box-shadow: 1px 2px 6px rgba(0,0,0,0.28);
    overflow: hidden;
  }
  .ornament-strip {
    position: absolute; left: 0; top: 0;
    width: 210px; height: 1179px;
    background: linear-gradient(90deg, var(--pattern-edge), var(--pattern-tone) 50%, var(--pattern-edge));
  }
  .brand {
    position: absolute; left: 524px; top: 20px; width: 290px;
    text-align: center;
  }
  .brand-square {
    width: 76px; height: 76px; margin: 0 auto 18px;
    background: var(--brand-green);
  }
  .brand-name {
    font-size: 40px; font-weight: 400; line-height: 1;
    color: var(--brand-grey);
  }
  .footer-block {
    position: absolute; line-height: 1.45;
  }
  .sender { left: 28px; top: 1014px; font-size: 16px; }
  .bank { left: 338px; top: 1016px; font-size: 15px; line-height: 1.5; }
  .tax { left: 584px; top: 1018px; font-size: 22px; line-height: 1.1; }
  .footer-block strong { font-weight: 700; }
  .accent-wedge {
    position: absolute; right: 0; bottom: 0; width: 306px; height: 15px;
  }
</style>
</head>
<body>
  <main class="letterhead">
    <div class="ornament-strip" role="img" aria-label="Vertikales graues Ornamentmuster am linken Rand"></div>

    <header class="brand">
      <div class="brand-square"></div>
      <div class="brand-name">Henrik Aldor</div>
    </header>

    <section class="footer-block sender">
      <strong>Nordlicht Medien</strong><br>
      Lindenallee 14<br>
      D-56070 Rheinfeld<br>
      Fon: +49 (0) 2631 482 510 00<br>
      Fax: +49 (0) 2631 482 510 22<br>
      E-Mail: kontakt@nordlicht-medien.de
    </section>

    <section class="footer-block bank">
      <strong>Bankverbindung:</strong><br>
      Nordlicht Medien<br>
      Kreissparkasse Rheinfeld<br>
      Kto.- Nr.: 539102<br>
      BLZ: 570 612 40<br>
      IBAN: DE12 5706 1240 0000 5391 02
    </section>

    <section class="footer-block tax">
      <strong>Finanzamt Rheinfeld</strong><br>
      USt. ID: DE418802357<br>
      St.-Nr.: 31/067/2815/9
    </section>

    <svg class="accent-wedge" viewBox="0 0 306 15" preserveAspectRatio="none" aria-hidden="true">
      <defs>
        <linearGradient id="wedgeGreen" x1="0" y1="0" x2="1" y2="0">
          <stop offset="0" stop-color="#9bd11f"/>
          <stop offset="1" stop-color="#c9ec6a"/>
        </linearGradient>
      </defs>
      <polygon points="18,0 306,0 306,15 0,15" fill="url(#wedgeGreen)"/>
    </svg>
  </main>
</body>
</html>
```